Clinc flyer

We need a flyer for our Physiotherapy and Acupuncture clinic to leave in a gym.
It needs the clinc logo and also:
"Free physiotherapy and acupuncture treament with an LPB claim." This should be larger text
"No referral needed" This should be under the previous text
"271c Tarevo Mall (entry via Brindle St)"
"582 3910"

```html
<!DOCTYPE html>
<html lang="en">
<head>
<meta charset="utf-8">
<title>Harbourline Clinic – Flyer</title>
<link rel="stylesheet" href="https://fonts.googleapis.com/css2?family=Bebas+Neue&family=Oswald:wght@400;500&display=swap">
<style>
  :root {
    --teal: #2a7b98;
    --teal-dark: #236d88;
    --sky: #29a9e0;
    --paper: #ffffff;
    --photo-light: #d9d9d9;
    --photo-dark: #8c8c8c;
    --skin-light: #efe3da;
    --skin-dark: #c9b3a4;
  }
  * { box-sizing: border-box; margin: 0; padding: 0; }
  html, body { width: 1056px; height: 1200px; overflow: hidden; background: var(--paper); }
  .flyer { position: relative; width: 1056px; height: 1200px; background: var(--paper); }
  .top-bar { position: absolute; left: 18px; top: 17px; width: 1017px; height: 14px; background: var(--teal); }

  .brand { position: absolute; left: 106px; top: 92px; display: flex; align-items: center; gap: 18px; }
  .brand-dot { width: 80px; height: 80px; border-radius: 50%; background: var(--teal); flex: none; }
  .brand-text { display: flex; flex-direction: column; }
  .brand-name { font-family: "Oswald", sans-serif; font-weight: 500; font-size: 50px; line-height: 1; color: var(--sky); }
  .brand-tagline { font-family: "Oswald", sans-serif; font-weight: 400; font-size: 15px; letter-spacing: 6px; color: var(--teal); margin-top: 8px; }

  .headline { position: absolute; left: 106px; top: 214px; font-family: "Bebas Neue", sans-serif; font-weight: 400; font-size: 86px; line-height: 82px; color: var(--teal); }
  .no-referral { position: absolute; left: 106px; top: 496px; padding: 6px 0 4px; border-top: 2px dotted var(--teal); border-bottom: 2px dotted var(--teal); font-family: "Bebas Neue", sans-serif; font-size: 44px; line-height: 40px; color: var(--sky); }

  .band { position: absolute; left: 0; top: 0; }
  .hero-photo { position: absolute; left: 470px; top: 515px; width: 565px; height: 572px; background: linear-gradient(160deg, var(--photo-light), var(--photo-dark)); }
  .treatment-photo { position: absolute; left: 115px; top: 613px; width: 260px; height: 260px; border-radius: 50%; border: 6px solid var(--sky); background: linear-gradient(135deg, var(--paper) 0%, var(--skin-light) 45%, var(--skin-dark) 100%); }

  .contact { position: absolute; left: 106px; color: var(--paper); font-family: "Bebas Neue", sans-serif; }
  .address { top: 908px; font-size: 48px; line-height: 46px; }
  .entry { top: 956px; font-size: 34px; line-height: 34px; }
  .call-label { top: 1014px; font-size: 27px; line-height: 28px; }
  .phone { top: 1040px; font-size: 86px; line-height: 80px; }

  .website { position: absolute; right: 110px; top: 1104px; font-family: "Oswald", sans-serif; font-weight: 400; font-size: 32px; line-height: 1; color: var(--teal-dark); }
</style>
</head>
<body>
<main class="flyer">
  <div class="top-bar"></div>

  <header class="brand">
    <span class="brand-dot"></span>
    <div class="brand-text">
      <span class="brand-name">Harbourline Clinic</span>
      <span class="brand-tagline">ACUPUNCTURE PHYSIOTHERAPY</span>
    </div>
  </header>

  <h1 class="headline">Free physiotherapy and<br>acupuncture treatment<br>with an LPB claim</h1>
  <p class="no-referral">No referral needed</p>

  <svg class="band" width="1056" height="1200" viewBox="0 0 1056 1200" aria-hidden="true">
    <polygon points="18,774 517,774 559,716 1035,716 1035,1087 559,1087 517,1141 18,1141" fill="var(--teal)"/>
    <polyline points="18,774 517,774 559,716 1035,716" fill="none" stroke="var(--sky)" stroke-width="5"/>
    <polyline points="517,1141 559,1087 1035,1087" fill="none" stroke="var(--sky)" stroke-width="5"/>
    <line x1="18" y1="1141" x2="517" y2="1141" stroke="var(--sky)" stroke-width="5"/>
  </svg>

  <div class="hero-photo" role="img" aria-label="Photo of a man from behind holding his neck and lower back, with red pain highlights"></div>
  <div class="treatment-photo" role="img" aria-label="Photo of a practitioner placing an acupuncture needle in a patient's back"></div>

  <p class="contact address">271C Tarevo Mall</p>
  <p class="contact entry">(Entry via Brindle St)</p>
  <p class="contact call-label">Call to make an appointment</p>
  <p class="contact phone">582 3910</p>

  <p class="website">www.harbourlinephysio.co.nz</p>
</main>
</body>
</html>
```